Psychotherapy Website - Based in London

I am a newly trained psychotherapist and need a new website for www.rosalindfaber.co.uk.

I offer therapy for addiction, relationships, trauma and many other issues people face in their lives.

I want the website to be welcoming, gentle, feminine and for people to feel safe.

I do not like a page site that scrolls through sections, rather each page should be separate. Here some examples that i like. Sectional rather than scrolled.

https://www.hettiemarsh.com/
https://www.thequietwardrooms.com/

The imagery should be around pink using the flower in the logo / wording and around the site:

Here is a link to the flower for ideas:
https://www.pictofind.net/search?q=pink+gerbera&rlz=2D4KQTW_en-GBGB415GB415&source=lnms&tbm=isch&sa=X&ved=7cvQRtrk482h3PxZTuKLmeNBwXW_1AtXpVlKDbOQBmFLB&biw=1500&bih=889&dpr=2

RosalindFaber
Compassionate Psychotherapy

Is the logo and subheader for the website. Please use a typeface for the name that is appealing and professional.

Type face similar NOT EXLUSIVLY - JUST AN IDEA like this:
https://glowtonicstudio.com/

Basic business card i created as a rough idea below.

I have also added the website copy.

The headers are

Homepage
About Me
Therapy
Common Questions
Blog
Contact Me

Target Market(s)

Clients who are dealing with stress, trauma, pain, addiction

Industry/Entity Type

Therapy and Psychology

Coding

Coded - Design and coding required

Number of Pages Required

5+ page

Font styles to use
Serif
Sans Serif
Script

Colors
0054AA
0677BA
7BADD7
CADEEF
E8F1F8
0094D4
00A9DD
6FCCEA
C7EBF8
E9F6FB
E54698
E96AAD
F1A4CE
F9D9EA
FCEFF6

Requirements
Must have
• Pink Gerbera Flower integrated into design
Nice to have
• Images but not to stock imagery. Needs to look authentic and natural
Should not have
• Stock images of people. Images are important but needs to feel REAL

```html
<!DOCTYPE html>
<html lang="en">
<head>
<meta charset="utf-8">
<title>Rosalind Faber – Compassionate Psychotherapy</title>
<link href="https://fonts.googleapis.com/css2?family=Rubik:wght@400;500;600&family=Yellowtail&family=Damion&display=swap" rel="stylesheet">
<style>
:root{
  --pink:#e5287f;
  --pink-soft:#fbd9e9;
  --pink-field:#fce3ef;
  --maroon:#8c1150;
  --ink:#2a2a2a;
  --white:#ffffff;
  --script:"Yellowtail","Damion",cursive;
  --sans:"Rubik",sans-serif;
}
*{box-sizing:border-box;margin:0;padding:0}
html,body{width:1200px;height:4066px;overflow:hidden;background:var(--white)}
body{position:relative;font-family:var(--sans);color:var(--ink);font-size:13px;line-height:17px}
.abs{position:absolute}
.nowrap{white-space:nowrap}
.script{font-family:var(--script);color:var(--pink);font-weight:400;letter-spacing:0}
.swoosh{position:absolute;display:block}
.flower-area{position:absolute;border-radius:50%;background:radial-gradient(ellipse at 45% 45%,#e2377f 0%,#ec4f93 35%,#f27aae 62%,rgba(248,170,205,.6) 80%,rgba(255,255,255,0) 100%)}
.btn{position:absolute;display:flex;align-items:center;justify-content:center;border-radius:22px;font-size:11px;font-weight:600;letter-spacing:.5px;text-transform:uppercase;color:var(--white);background:linear-gradient(90deg,var(--maroon),var(--pink))}
/* header */
.brand{left:107px;top:38px}
.brand-name{font-family:var(--script);color:var(--pink);font-size:46px;line-height:1}
.brand-sub{font-size:8.5px;font-weight:600;letter-spacing:.4px;margin-top:6px;text-transform:uppercase}
.nav{left:590px;top:52px;display:flex;gap:26px;font-size:10.5px;font-weight:500;text-transform:uppercase;letter-spacing:.3px;z-index:2}
.nav .active{color:var(--pink)}
.hero-flower{left:480px;top:-70px;width:790px;height:740px}
.hero-title{left:107px;top:236px;font-size:27px;font-weight:500;line-height:32px}
.hero-title .script{font-size:36px}
.hero-text{left:107px;top:352px;font-size:13px;font-weight:500;line-height:17px}
/* intro panel */
.intro{left:106px;top:621px;width:988px;height:384px;background:var(--pink-soft);border-radius:30px}
.intro-title{left:178px;top:672px;font-size:19px;font-weight:500;display:flex;align-items:baseline;gap:12px}
.intro-title .script{font-size:33px}
.intro-copy{left:178px;top:745px;font-size:13px}
.intro-copy p{margin-bottom:17px}
.intro-photo{left:850px;top:742px;width:284px;height:284px;border-radius:50%;border:2px solid var(--pink);padding:10px;background:var(--white)}
.intro-photo div{width:100%;height:100%;border-radius:50%;background:linear-gradient(160deg,#e4e0da,#a89886)}
/* about */
.about-photo{left:104px;top:1150px;width:462px;height:462px;border-radius:50%;border:2px solid var(--pink);padding:18px}
.about-photo div{width:100%;height:100%;border-radius:50%;background:linear-gradient(170deg,#d9cdb2 0%,#e3bba8 45%,#e0588f 80%)}
.about-title{left:636px;top:1180px;font-size:19px;font-weight:500;display:flex;align-items:baseline;gap:10px}
.about-title .script{font-size:35px}
.about-copy{left:636px;top:1255px;font-size:13px}
.about-copy p{margin-bottom:17px}
/* therapy band */
.therapy{left:0;top:1678px;width:1200px;height:362px;border-radius:40px 0 0 0;background:linear-gradient(90deg,#e73886 0%,#b81a63 55%,#8c1150 100%)}
.therapy-flower{left:815px;top:1640px;width:420px;height:510px}
.t-head{left:107px;top:1730px;color:var(--white)}
.t-head .script{color:var(--white);font-size:36px}
.t-copy{left:107px;top:1811px;color:var(--white);font-size:13px}
.t-btn{left:106px;top:1955px;width:194px;height:39px;background:none;border:1.5px solid var(--white)}
.help-title{left:534px;top:1740px;color:var(--white);font-size:18px;font-weight:500;display:flex;align-items:baseline;gap:10px}
.help-title .script{color:var(--white);font-size:33px}
.help-list{left:532px;top:1810px;list-style:none;color:var(--white);font-size:13px}
.help-list li{height:21px;display:flex;align-items:center;gap:7px}
.help-list li::before{content:"";border-left:5px solid var(--white);border-top:4px solid transparent;border-bottom:4px solid transparent}
.view-all{left:545px;top:1962px;color:var(--white);font-size:13px;font-weight:600;border-bottom:2px solid var(--white);padding-bottom:3px}
/* faq */
.sec-title{left:0;width:1200px;text-align:center;font-size:19px;font-weight:500}
.sec-title .script{font-size:36px;margin-left:6px}
.faq{left:212px;width:776px;background:var(--pink-soft);border-radius:6px;padding:0 36px}
.faq h3{font-size:13.5px;font-weight:600;height:76px;display:flex;align-items:center;justify-content:space-between}
.faq p{font-size:13px;margin-top:-16px;white-space:nowrap}
.chev{width:20px;height:20px;border:1.5px solid var(--ink);border-radius:50%;display:flex;align-items:center;justify-content:center}
.faq-flower{left:-100px;top:2460px;width:310px;height:330px}
/* blog */
.blog{left:0;top:2654px;width:1200px;height:529px;border-radius:0 40px 40px 40px;background:linear-gradient(90deg,#8c1150 0%,#c2206b 60%,#e5307f 100%)}
.blog-card{width:477px;color:var(--white)}
.blog-card .img{height:176px;background:linear-gradient(90deg,#ecadc8 0%,#b98193 30%,#7a4650 50%,#c97fa0 75%,#ecb0c9 100%)}
.blog-card h4{font-size:13.5px;font-weight:600;margin-top:26px}
.blog-card p{font-size:13px;margin-top:14px;white-space:nowrap}
.blog-card a{display:flex;align-items:center;gap:10px;margin-top:17px;font-size:12.5px;font-weight:600;text-transform:uppercase;color:var(--white);text-decoration:none}
.blog-card a::before{content:"";border-left:5px solid var(--white);border-top:4px solid transparent;border-bottom:4px solid transparent}
/* contact */
.field{background:var(--pink-field);font-size:13px;padding:12px 12px;border-radius:2px}
/* footer */
.footer{left:0;top:3710px;width:1200px;height:356px;border-radius:40px 0 0 0;background:linear-gradient(90deg,#e0307f 0%,#b81a63 60%,#8c1150 100%)}
.footer-flower{left:1015px;top:3700px;width:330px;height:420px}
.f-brand{left:137px;top:3763px}
.f-brand .brand-name{color:var(--white);font-size:40px}
.f-brand .brand-sub{color:var(--white)}
.socials{left:177px;top:3861px;display:flex;gap:5px}
.socials span{width:20px;height:20px;border-radius:50%;background:var(--white)}
.f-head{top:3785px;font-size:10.5px;font-weight:600;text-transform:uppercase;color:var(--white);letter-spacing:.4px}
.f-head::after{content:"";display:block;width:118px;height:1px;background:rgba(255,255,255,.5);margin-top:9px}
.f-links{left:423px;top:3828px;list-style:none;font-size:11px;color:var(--white);line-height:17px}
.f-item{font-size:11px;color:var(--white);display:flex;gap:10px;line-height:17px}
.copyright{left:0;top:3999px;width:1200px;text-align:center;font-size:10.5px;font-weight:500;color:var(--white)}
</style>
</head>
<body>

<header>
  <div class="abs brand">
    <div class="brand-name">Rosalind Faber</div>
    <div class="brand-sub">Psychotherapeutic Counselor</div>
  </div>
  <nav class="abs nav">
    <span class="active">Home</span><span>About Me</span><span>Therapy</span><span>Common Questions</span><span>Blog</span><span>Contact Me</span>
  </nav>
</header>

<div class="flower-area hero-flower" role="img" aria-label="Photo of a large pink gerbera flower"></div>

<section>
  <h1 class="abs hero-title nowrap">Taking the first steps towards<br>engaging in therapy can be<br>a very <span class="script">personal journey</span></h1>
  <p class="abs hero-text nowrap">Whilst, it can be challenging, I will ensure to<br>make this journey as safe and as comfortable<br>for you as possible.</p>
  <a class="btn" style="left:106px;top:428px;width:194px;height:38px">Schedule a session</a>
</section>

<section>
  <div class="abs intro"></div>
  <h2 class="abs intro-title"><span class="script">Psychotherapy</span> can help you see your current situation in new light, depth and clarity.</h2>
  <svg class="swoosh" style="left:176px;top:712px" width="160" height="14"><path d="M2 10 Q80 2 158 6" stroke="#e5287f" stroke-width="2" fill="none"/></svg>
  <div class="abs intro-copy nowrap">
    <p>It can change old and unhelpful perspectives and feelings about yourself and your life,<br>and ultimately help you make positive changes. It might be the most important journey<br>you'll ever make. I provide a and non-judgmental space where any issues can be explored<br>in complete confidentiality.</p>
    <p>My practice is based in Richmond, where the room is homely, comfortable and welcoming.<br>I believe a good environment contributes to great therapy. Alternately, I am also available<br>to provide therapy online, if this environment is more accommodating for my clients.</p>
    <p>I am passionate about improving mental health and committed to offering therapy to all<br>individuals regardless of their age, race, culture, disability, sexual orientation, or socio-<br>economic background.</p>
  </div>
  <div class="abs intro-photo"><div role="img" aria-label="Photo of a client seated in a calm therapy room"></div></div>
</section>

<section>
  <div class="abs about-photo"><div role="img" aria-label="Portrait photo of the therapist"></div></div>
  <h2 class="abs about-title">About <span class="script">Rosalind Faber</span></h2>
  <svg class="swoosh" style="left:700px;top:1218px" width="180" height="14"><path d="M2 10 Q90 2 178 6" stroke="#e5287f" stroke-width="2" fill="none"/></svg>
  <div class="abs about-copy nowrap">
    <p>I have over 10 years' experience of dealing with addictions.<br>Addictions are often more of a solution to fear and emotional<br>pain. However, eventually the addiction causes more problems.<br>I know recovery is possible with the right support.</p>
    <p>I have also had some twenty years of experience of dealing with<br>mental health issues such as depression, anxiety, complex PTSD<br>and trauma. It is possible to manage these issues and live a full<br>life.</p>
    <p>I have worked in the voluntary sector as a Listening Line volunteer<br>and I am currently a therapist for Calm Minds Trust.</p>
  </div>
  <a class="btn" style="left:635px;top:1487px;width:192px;height:38px">More about me</a>
</section>

<section>
  <div class="abs therapy"></div>
  <div class="flower-area therapy-flower" role="img" aria-label="Photo of a pink gerbera flower"></div>
  <h2 class="abs t-head"><span class="script">Therapy</span></h2>
  <svg class="swoosh" style="left:110px;top:1780px" width="80" height="14"><path d="M2 10 Q40 2 78 6" stroke="#fff" stroke-width="2" fill="none"/></svg>
  <p class="abs t-copy nowrap">Therapy can help you to develop ways of coping<br>better and overcoming issues you may feel are<br>holding you back. I can help you find and develop<br>your personal strengths and help identify what<br>is meaningful to you in life. By doing this, you<br>will be able to move towards the kind of life you<br>would like to live.</p>
  <a class="btn t-btn">Find out more</a>
  <h2 class="abs help-title">What we <span class="script">can help with</span></h2>
  <svg class="swoosh" style="left:620px;top:1776px" width="150" height="14"><path d="M2 10 Q75 2 148 6" stroke="#fff" stroke-width="2" fill="none"/></svg>
  <ul class="abs help-list">
    <li>Addiction</li><li>Bullying</li><li>Depression</li><li>Fear</li><li>HIV</li><li>Loss of Meaning</li><li>Problems with Motivation/Focus</li>
  </ul>
  <span class="abs view-all">View all</span>
</section>

<section>
  <h2 class="abs sec-title" style="top:2110px">Common <span class="script">Questions</span></h2>
  <svg class="swoosh" style="left:590px;top:2150px" width="110" height="14"><path d="M2 10 Q55 2 108 6" stroke="#e5287f" stroke-width="2" fill="none"/></svg>
  <div class="abs faq" style="top:2203px;height:197px">
    <h3>How long will I need therapy for? <span class="chev"><svg width="10" height="6"><path d="M1 5 L5 1 L9 5" stroke="#2a2a2a" stroke-width="1.5" fill="none"/></svg></span></h3>
    <p>Therapy can last anywhere from one session to several months or even years. It all depends on what<br>you want and need. Some people come to therapy with a very specific problem they need to solve<br>and might find that one or two sessions is sufficient. Other people come to therapy with more<br>complicated issues they are grappling with and may feel they need a few months or more to<br>understand and resolve their issues. Other people come with long-standing problems or difficult<br>feelings and may benefit from longer-term therapy.</p>
  </div>
  <div class="abs faq" style="top:2416px;height:76px">
    <h3>How long are the sessions? <span class="chev"><svg width="10" height="6"><path d="M1 1 L5 5 L9 1" stroke="#2a2a2a" stroke-width="1.5" fill="none"/></svg></span></h3>
  </div>
  <div class="abs faq" style="top:2507px;height:76px">
    <h3>How much is each session? <span class="chev"><svg width="10" height="6"><path d="M1 1 L5 5 L9 1" stroke="#2a2a2a" stroke-width="1.5" fill="none"/></svg></span></h3>
  </div>
</section>

<section>
  <div class="abs blog"></div>
  <div class="flower-area faq-flower" role="img" aria-label="Photo of a pink gerbera flower"></div>
  <h2 class="abs sec-title" style="top:2710px;color:#fff">Latest <span class="script" style="color:#fff">Blog</span></h2>
  <svg class="swoosh" style="left:595px;top:2750px" width="80" height="14"><path d="M2 10 Q40 2 78 6" stroke="#fff" stroke-width="2" fill="none"/></svg>
  <article class="abs blog-card" style="left:106px;top:2804px">
    <div class="img" role="img" aria-label="Photo of a woman resting her head on her arms"></div>
    <h4>Trauma and the bears – a fable</h4>
    <p>Once upon a time there were humans on the savannah. It's a<br>dangerous world. We need to find food, we need to protect ourselves<br>from predators, we need shelter, we need to find a mate.</p>
    <a>Read more</a>
  </article>
  <article class="abs blog-card" style="left:617px;top:2804px">
    <div class="img" role="img" aria-label="Photo of a woman resting her head on her arms"></div>
    <h4>Why the symptoms of trauma make sense</h4>
    <p>I looked again at the list of symptoms. It was long, and overwhelming,<br>and ran to more than two pages. 'Signs you've been traumatised'<br>promised the infographic.</p>
    <a>Read more</a>
  </article>
</section>

<section>
  <h2 class="abs sec-title" style="top:3256px">Contact <span class="script">Me</span></h2>
  <svg class="swoosh" style="left:608px;top:3294px" width="68" height="14"><path d="M2 10 Q34 2 66 6" stroke="#e5287f" stroke-width="2" fill="none"/></svg>
  <div class="abs field" style="left:280px;top:3339px;width:312px;height:50px">First Name*</div>
  <div class="abs field" style="left:606px;top:3339px;width:314px;height:50px">Last Name*</div>
  <div class="abs field" style="left:280px;top:3404px;width:312px;height:49px">Email Address*</div>
  <div class="abs field" style="left:606px;top:3404px;width:314px;height:49px">Phone Number</div>
  <div class="abs field" style="left:280px;top:3467px;width:640px;height:119px">Message*</div>
  <a class="btn" style="left:502px;top:3601px;width:194px;height:39px">Submit</a>
</section>

<footer>
  <div class="abs footer"></div>
  <div class="flower-area footer-flower" role="img" aria-label="Photo of a pink gerbera flower"></div>
  <div class="abs f-brand">
    <div class="brand-name">Rosalind Faber</div>
    <div class="brand-sub">Psychotherapeutic Counselor</div>
  </div>
  <div class="abs socials"><span></span><span></span><span></span><span></span><span></span></div>
  <div class="abs f-head" style="left:423px">Quick Links</div>
  <ul class="abs f-links"><li>Home</li><li>About Me</li><li>Therapy</li><li>Common Questions</li><li>Blog</li><li>Contact Me</li></ul>
  <div class="abs f-head" style="left:622px">Contactme</div>
  <div class="abs f-item" style="left:622px;top:3828px">
    <svg width="10" height="13" viewBox="0 0 10 13"><path d="M5 0C2.2 0 0 2.2 0 5c0 3.6 5 8 5 8s5-4.4 5-8c0-2.8-2.2-5-5-5z" fill="#fff"/><circle cx="5" cy="5" r="1.8" fill="#c2206b"/></svg>
    <span>Elmfield Community Centre<br>27 Larchmont Road<br>East Sheen<br>SW14 9QX</span>
  </div>
  <div class="abs f-item" style="left:854px;top:3828px">
    <svg width="12" height="12" viewBox="0 0 12 12"><path d="M2.5 0.5l2 2.5-1.2 1.5c.8 1.6 2.1 2.9 3.7 3.7L8.5 7l2.5 2-1 2.5C5 11 1 7 .5 2z" fill="#fff"/></svg>
    <span>07700 900418</span>
  </div>
  <div class="abs f-item" style="left:854px;top:3860px">
    <svg width="12" height="9" viewBox="0 0 12 9"><rect width="12" height="9" fill="#fff"/><path d="M0 0l6 5 6-5" stroke="#c2206b" fill="none"/></svg>
    <span>hello@rosalindfaber.co.uk</span>
  </div>
  <p class="abs copyright">Copyright © 2021 Rosalind Faber | All Right Reserved.</p>
</footer>

</body>
</html>
```